Gourmet cookie company needs a label designed

We need a label designed for a new cookie company. We make mini cookies. The labels will be placed on either white tins or clear containers. We would like some bright and eye catching label although not child like. Our target customer is adults not kids.
Any color/colors acceptable. The initial label will be a square 4" label but the design should also be able to be formatted to fit on a round label as well in the future.

Text on label: Rosalind's Wafer Crumb Company; Chocolate Chip; All Natural; New Wt. 8.0oz

```html
<!DOCTYPE html>
<html lang="en">
<head>
<meta charset="utf-8">
<title>Rosalind's Wafer Crumb Company – Chocolate Chip Label</title>
<link rel="stylesheet" href="https://fonts.googleapis.com/css2?family=Gorditas:wght@700&family=Josefin+Sans:wght@600&display=swap">
<style>
  :root {
    --stripe-light: #f2d6cc;
    --stripe-dark: #d19f8c;
    --cookie-top: #7a0803;
    --cookie-bottom: #3a0d0a;
    --cookie-rim: #ffffff;
    --mound: #8a2f22;
    --text-light: #ffffff;
  }
  html, body {
    margin: 0;
    padding: 0;
    width: 1200px;
    height: 1200px;
    overflow: hidden;
    background: var(--stripe-light);
  }
  .label {
    display: block;
    width: 1200px;
    height: 1200px;
  }
  .stripe-light { fill: var(--stripe-light); }
  .stripe-dark { fill: var(--stripe-dark); }
  .mound { fill: var(--mound); }
  .cookie-rim { fill: var(--cookie-rim); }
  .cookie-body { fill: url(#cookieShade); }
  .brand-name {
    font-family: "Gorditas", "Georgia", serif;
    font-weight: 700;
    fill: var(--text-light);
  }
  .brand-name--main { font-size: 118px; }
  .brand-name--sub { font-size: 46px; }
  .flavour {
    font-family: "Gorditas", "Georgia", serif;
    font-weight: 700;
    font-size: 34px;
    fill: var(--text-light);
  }
  .claim {
    font-family: "Josefin Sans", "Helvetica", sans-serif;
    font-weight: 600;
    font-size: 21px;
    letter-spacing: 6px;
    fill: var(--text-light);
  }
  .net-weight {
    font-family: "Josefin Sans", "Helvetica", sans-serif;
    font-weight: 600;
    font-size: 26px;
    font-variant: small-caps;
    fill: var(--text-light);
  }
</style>
</head>
<body>
<svg class="label" viewBox="0 0 1200 1200" xmlns="http://www.w3.org/2000/svg">
  <defs>
    <linearGradient id="cookieShade" x1="0" y1="0" x2="0" y2="1">
      <stop offset="0" stop-color="#7a0803"/>
      <stop offset="1" stop-color="#3a0d0a"/>
    </linearGradient>
  </defs>

  <g class="stripes">
    <rect class="stripe-light" x="0" y="0" width="1200" height="1200"/>
    <rect class="stripe-dark" x="75" y="0" width="150" height="1200"/>
    <rect class="stripe-dark" x="375" y="0" width="150" height="1200"/>
    <rect class="stripe-dark" x="675" y="0" width="150" height="1200"/>
    <rect class="stripe-dark" x="975" y="0" width="150" height="1200"/>
  </g>

  <path class="mound" role="img" aria-label="Dotted chocolate-chip pattern filling the lower mound"
        d="M0 912 Q600 660 1200 912 L1200 1200 L0 1200 Z"/>

  <g class="cookie-badge">
    <circle class="cookie-rim" cx="600" cy="595" r="362"/>
    <circle class="cookie-body" cx="600" cy="595" r="346"/>
  </g>

  <g class="brand" text-anchor="middle">
    <text class="brand-name brand-name--main" x="600" y="720">Rosalind's</text>
    <text class="brand-name brand-name--sub" x="600" y="790">Wafer Crumb Company</text>
  </g>

  <g class="product" text-anchor="middle">
    <text class="flavour" x="600" y="858">Chocolate Chip</text>
    <text class="claim" x="603" y="891">ALL NATURAL</text>
  </g>

  <text class="net-weight" x="600" y="1167" text-anchor="middle">New Wt. 8.0oz</text>
</svg>
</body>
</html>
```